International Trading Company, 'KIRO' needs a Business Card

The company name is "KIRO" and it has own logo design.
I'd like to use its logo on this business card.
I need two side Business Card.
I'll look forward to your great design.
Thank you very much in advance.

Contact Information for Business Card

Company Name : Kiro Harbour Limited
Information Example
Dorian Pallister
Mobile(use icon please) : 1 (212) 555-0143
Tel(use icon please) : 1 (212) 555-0178
Email(use icon please) : dorian27@kiroharbour-mail.com
Address(use icon please) : 482 Halden Ave, New York, NY 10160, USA

```html
<!DOCTYPE html>
<html lang="en">
<head>
<meta charset="utf-8">
<title>Kiro Harbour Limited — Business Card</title>
<link rel="stylesheet" href="https://fonts.googleapis.com/css2?family=Montserrat:wght@600&family=Merriweather:wght@400;700&display=swap">
<style>
  :root {
    --page-bg: #e4e4e4;
    --card-dark: #0e0e0e;
    --card-mid: #2c2c2c;
    --card-light: #3a3a3a;
    --band: rgba(255, 255, 255, 0.05);
    --band-dark: rgba(0, 0, 0, 0.35);
    --ink-white: #f4f4f4;
    --ink-soft: #d9d9d9;
    --icon-glyph: #1d1d1d;
  }
  * { margin: 0; padding: 0; box-sizing: border-box; }
  html, body {
    width: 1200px; height: 1092px; overflow: hidden;
    background: var(--page-bg);
  }
  .sheet {
    width: 1200px; height: 1092px;
    display: flex; align-items: center; justify-content: center; gap: 40px;
  }
  .card {
    position: relative; width: 540px; height: 327px; overflow: hidden;
    background: radial-gradient(ellipse at 45% 45%, var(--card-light) 0%, var(--card-mid) 40%, var(--card-dark) 100%);
    box-shadow: 0 2px 6px rgba(0,0,0,0.25);
  }
  .card-bands { position: absolute; inset: 0; width: 100%; height: 100%; }
  .brand-word {
    font-family: "Montserrat", sans-serif; font-weight: 600;
    color: var(--ink-white); line-height: 1;
  }
  /* front */
  .front-logo { position: absolute; left: 88px; top: 108px; }
  .front-logo .brand-mark { font-size: 118px; letter-spacing: 2px; }
  .front-logo .brand-name {
    display: block; margin-top: 10px; font-size: 27px; letter-spacing: 1px;
    text-transform: uppercase;
  }
  /* back */
  .contact-list {
    position: absolute; left: 56px; top: 60px; list-style: none;
    font-family: "Merriweather", serif; font-size: 17px; color: var(--ink-soft);
  }
  .contact-item { display: flex; align-items: flex-start; gap: 10px; margin-bottom: 11px; }
  .contact-item svg { flex: none; width: 26px; height: 26px; }
  .contact-text { line-height: 26px; }
  .contact-name { font-weight: 700; font-size: 19px; color: var(--ink-white); }
  .street { font-weight: 700; color: var(--ink-white); }
  .address-text { line-height: 24px; }
  .back-logo { position: absolute; right: 44px; bottom: 44px; font-size: 44px; letter-spacing: 1px; }
</style>
</head>
<body>
<main class="sheet">

  <section class="card card-front" aria-label="Business card front">
    <svg class="card-bands" viewBox="0 0 540 327" preserveAspectRatio="none" aria-hidden="true">
      <polygon points="0,0 70,0 210,327 130,327" fill="var(--band)"/>
      <polygon points="0,60 0,190 120,0 60,0" fill="var(--band-dark)"/>
      <polygon points="330,0 420,0 120,327 40,327" fill="var(--band)"/>
      <polygon points="540,120 540,327 420,327" fill="var(--band-dark)"/>
    </svg>
    <div class="front-logo">
      <span class="brand-word brand-mark">KIRO</span>
      <span class="brand-word brand-name">Kiro Harbour Limited</span>
    </div>
  </section>

  <section class="card card-back" aria-label="Business card back">
    <svg class="card-bands" viewBox="0 0 540 327" preserveAspectRatio="none" aria-hidden="true">
      <polygon points="330,0 430,0 540,110 540,230" fill="var(--band)"/>
      <polygon points="540,90 540,200 400,327 290,327" fill="var(--band-dark)"/>
      <polygon points="460,0 540,0 540,60" fill="var(--band-dark)"/>
    </svg>
    <ul class="contact-list">
      <li class="contact-item">
        <svg viewBox="0 0 26 26" aria-hidden="true"><circle cx="13" cy="13" r="13" fill="var(--ink-white)"/><circle cx="13" cy="10" r="4" fill="var(--icon-glyph)"/><path d="M6 20c1-4 4-5.5 7-5.5s6 1.5 7 5.5z" fill="var(--icon-glyph)"/></svg>
        <span class="contact-text contact-name">Dorian Pallister</span>
      </li>
      <li class="contact-item">
        <svg viewBox="0 0 26 26" aria-hidden="true"><circle cx="13" cy="13" r="13" fill="var(--ink-white)"/><path d="M8 6.5l3 0 1.2 3.5-2 1.3c.9 2 2.5 3.6 4.5 4.5l1.3-2 3.5 1.2 0 3c-6.5 .3-11.8-5-11.5-11.5z" fill="var(--icon-glyph)"/></svg>
        <span class="contact-text">1 (212) 555-0143</span>
      </li>
      <li class="contact-item">
        <svg viewBox="0 0 26 26" aria-hidden="true"><circle cx="13" cy="13" r="13" fill="var(--ink-white)"/><rect x="9" y="5.5" width="8" height="15" rx="1.5" fill="var(--icon-glyph)"/><rect x="10.3" y="7.5" width="5.4" height="9" fill="var(--ink-white)"/></svg>
        <span class="contact-text">1 (212) 555-0178</span>
      </li>
      <li class="contact-item">
        <svg viewBox="0 0 26 26" aria-hidden="true"><circle cx="13" cy="13" r="13" fill="var(--ink-white)"/><rect x="6.5" y="8.5" width="13" height="9" fill="var(--icon-glyph)"/><path d="M6.5 8.5l6.5 5 6.5-5" fill="none" stroke="var(--ink-white)" stroke-width="1.2"/></svg>
        <span class="contact-text">dorian27@kiroharbour-mail.com</span>
      </li>
      <li class="contact-item">
        <svg viewBox="0 0 26 26" aria-hidden="true"><circle cx="13" cy="13" r="13" fill="var(--ink-white)"/><path d="M13 5a5 5 0 0 1 5 5c0 4-5 10-5 10s-5-6-5-10a5 5 0 0 1 5-5z" fill="var(--icon-glyph)"/><circle cx="13" cy="10" r="1.8" fill="var(--ink-white)"/></svg>
        <span class="contact-text address-text">482 <span class="street">Halden Ave</span>, New York,<br>NY 10160, USA</span>
      </li>
    </ul>
    <span class="brand-word back-logo">KIRO</span>
  </section>

</main>
</body>
</html>
```